Innovative cost reduction consultant needs to build a group of technical advisors

We need to share our message and compassion for developing cost reduction in the automotive industry. We create opportunities for immediate innovation, by developing cost reduction solutions across suppliers with related process. Attached is an existing Power Point, but it needs improvement. Most of all, a good compelling story, why experts should join us.

Target Market(s)

Automotive industry, supply chain management

Industry/Entity Type

Automotive

Font styles to use
Serif
Sans Serif

Requirements
Must have
• Better visual graphics. There are a few, but they are not as visually appearing as I would like. A graphic with data should have a better visual impact then the ones that I created. I would like to share the message, that I am providing a solution for the automotive industry. The goal is to reduce costs and improve supplier and OEM relationships. The objective is to do so by creating opportunities for immediate innovation, by developing cost reduction solutions across suppliers with related processes. This message may need a visual graphic, which is missing from the presentation.
Nice to have
• Challenge my story and presentation. Does this make sense to you, and what is your opinions of the subject. Or, a relevant news source to validate the story.
Should not have
• I have not decided on the name of the venture or logo. So, let's just use my name as the source or writer. Marcus Trevell, Cost Reduction Specialist. Thanks,

```html
<!DOCTYPE html>
<html lang="en">
<head>
<meta charset="utf-8">
<title>Supplier Cost Reduction – Slide Overview</title>
<link href="https://fonts.googleapis.com/css2?family=Roboto:wght@300;400;500;700&display=swap" rel="stylesheet">
<style>
  :root{
    --blue:#0ea7eb;
    --blue-dark:#0a8fd0;
    --blue-soft:#5cc6f2;
    --pink:#e6165a;
    --ink:#333;
    --ink-soft:#666;
    --gray:#8a8a8a;
    --gray-dark:#4a4a4a;
    --money:#3aa53a;
    --paper:#fff;
  }
  html,body{margin:0;padding:0;width:1200px;height:1200px;overflow:hidden;background:var(--paper);}
  body{position:relative;font-family:'Roboto',sans-serif;}
  .slide{position:absolute;width:361px;height:203px;background:var(--paper);box-shadow:0 1px 4px rgba(0,0,0,.18);}
  .slide svg{display:block;width:361px;height:203px;}
  .c1{left:30px}.c2{left:417px}.c3{left:806px}
  .r1{top:34px}.r2{top:262px}.r3{top:490px}.r4{top:718px}.r5{top:945px}

  svg text{font-family:'Roboto',sans-serif;}
  .hdr{fill:var(--blue);}
  .band{fill:var(--blue);}
  .ttl{fill:#fff;font-size:13px;font-weight:400;}
  .pin{fill:var(--pink);stroke:#fff;stroke-width:1.5;}
  .pin-num{fill:#fff;font-size:5.5px;text-anchor:middle;}
  .body{fill:var(--ink);font-size:7px;}
  .small{fill:var(--ink);font-size:6px;}
  .on-blue{fill:#fff;}
  .mid{text-anchor:middle;}
  .b{font-weight:700;}
  .pill-txt{fill:#fff;font-size:6px;text-anchor:middle;}
  .blue-fill{fill:var(--blue);}
  .gray-fill{fill:var(--gray);}
  .dark-fill{fill:var(--gray-dark);}
  .money{fill:var(--money);font-weight:700;}
  .photo{fill:url(#carTone);}
  .news-title{fill:#111;font-size:21px;font-weight:500;letter-spacing:-.6px;}
  .news-sub{fill:var(--blue-dark);font-size:5.4px;font-weight:500;}
  .news-txt{fill:#444;font-size:4.1px;}
  .venn{fill:var(--blue);fill-opacity:.55;stroke:#fff;stroke-width:1;}
  .step-front{fill:var(--blue);}
  .step-side{fill:var(--blue-dark);}
  .step-top{fill:#5fc9f5;}
  .num-ring{fill:#fff;stroke:var(--blue);stroke-width:1.2;}
  .num{fill:var(--blue);font-size:9px;text-anchor:middle;}
  .link{stroke:#bbb;stroke-width:.7;fill:none;}
</style>
</head>
<body>

<svg width="0" height="0" style="position:absolute">
  <defs>
    <linearGradient id="carTone" x1="0" y1="0" x2="0" y2="1">
      <stop offset="0" stop-color="#8d929b"/><stop offset="1" stop-color="#3d4149"/>
    </linearGradient>
    <linearGradient id="carLight" x1="0" y1="0" x2="0" y2="1">
      <stop offset="0" stop-color="#f1f2f4"/><stop offset="1" stop-color="#b9bdc4"/>
    </linearGradient>
    <linearGradient id="mapTone" x1="0" y1="0" x2="1" y2="1">
      <stop offset="0" stop-color="#c9d7f0"/><stop offset=".5" stop-color="#f3c9b5"/><stop offset="1" stop-color="#bfe3c3"/>
    </linearGradient>
    <pattern id="heatA" width="56" height="14" patternUnits="userSpaceOnUse">
      <rect width="14" height="7" fill="#f4c542"/><rect x="14" width="14" height="7" fill="#e8534a"/>
      <rect x="28" width="14" height="7" fill="#8cc76a"/><rect x="42" width="14" height="7" fill="#f7e27a"/>
      <rect y="7" width="14" height="7" fill="#f08a4b"/><rect x="14" y="7" width="14" height="7" fill="#fbe9a6"/>
      <rect x="28" y="7" width="14" height="7" fill="#e8534a"/><rect x="42" y="7" width="14" height="7" fill="#a9d48a"/>
    </pattern>
    <pattern id="numLines" width="24" height="3.5" patternUnits="userSpaceOnUse">
      <rect x="2" y="1.2" width="16" height="1" fill="#9a9a9a"/>
    </pattern>
  </defs>
</svg>

<!-- Slide 1: cover -->
<div class="slide c1 r1">
  <svg viewBox="0 0 451 254">
    <rect x="72" y="29" width="50" height="11" rx="5.5" class="blue-fill"/>
    <text x="97" y="36.5" class="pill-txt" style="font-size:5.5px">2010</text>
    <path d="M154 29H291L297 34.5 291 40H154L160 34.5Z" class="blue-fill"/>
    <text x="226" y="36.5" class="pill-txt" style="font-size:5.5px">6 Year Forecast</text>
    <rect x="330" y="29" width="50" height="11" rx="5.5" class="blue-fill"/>
    <text x="355" y="36.5" class="pill-txt" style="font-size:5.5px">2016</text>
    <rect x="60" y="70" width="72" height="36" rx="12" class="photo" role="img" aria-label="Dark grey 2010 sedan"/>
    <rect x="304" y="60" width="93" height="54" rx="16" fill="url(#carLight)" role="img" aria-label="White 2016 sedan"/>
    <text x="154" y="95" class="money" font-size="24">$</text>
    <text x="180" y="95" class="money" font-size="22">$</text>
    <text x="205" y="95" class="money" font-size="19">$</text>
    <text x="228" y="95" class="money" font-size="16">$</text>
    <text x="248" y="95" class="money" font-size="13">$</text>
    <text x="264" y="95" class="money" font-size="11">$</text>
    <text x="278" y="95" class="money" font-size="9">$</text>
    <rect y="142" width="451" height="112" class="band"/>
    <circle cx="418" cy="144" r="11" class="pin"/><text x="418" y="146" class="pin-num">1</text>
    <text x="67" y="162" class="on-blue" font-size="7.6">Creating opportunities for immediate innovation,</text>
    <text x="67" y="173" class="on-blue" font-size="7.6">by developing cost reduction solutions across suppliers with related processes.</text>
    <text x="67" y="193" class="on-blue" font-size="8.5"><tspan font-size="5.5">By </tspan>Marcus Trevell,</text>
    <text x="67" y="206" class="on-blue" font-size="5.5">Cost Reduction Specialist</text>
    <rect x="65" y="215" width="71" height="11" rx="5.5" fill="#fff"/>
    <text x="100.5" y="222.5" font-size="5.5" fill="var(--blue)" text-anchor="middle">02 December, 2015</text>
  </svg>
</div>

<!-- Slide 2: Innovative supplier cost reduction -->
<div class="slide c2 r1">
  <svg viewBox="0 0 451 254">
    <rect class="hdr" width="451" height="53"/>
    <text x="40" y="30" class="ttl">Innovative Supplier Cost Reduction</text>
    <circle cx="418" cy="53" r="11" class="pin"/><text x="418" y="55" class="pin-num">6</text>
    <text x="225" y="79" class="small mid">The goal is an alignment of innovative cost reduction technology and cost</text>
    <text x="225" y="90" class="small mid">improvement requirements across the supplier group</text>
    <path d="M165 120 Q225 190 225 200 Q225 190 285 120Z" fill="#d8f0fc" stroke="var(--blue-soft)" stroke-width=".8"/>
    <ellipse cx="225" cy="120" rx="60" ry="12" fill="#eaf7fe" stroke="var(--blue-soft)" stroke-width=".8"/>
    <circle cx="201" cy="144" r="18" class="blue-fill" stroke="#fff" stroke-width="1"/>
    <text x="201" y="142" class="pill-txt" font-size="4.5">GAP</text><text x="201" y="147" class="pill-txt" font-size="4.5">Analysis</text>
    <circle cx="242" cy="132" r="17" class="blue-fill" stroke="#fff" stroke-width="1"/>
    <text x="242" y="131" class="pill-txt" font-size="4.5">Forecast</text><text x="242" y="136" class="pill-txt" font-size="4.5">data</text>
    <circle cx="229" cy="173" r="18" class="blue-fill" stroke="#fff" stroke-width="1"/>
    <text x="229" y="168" class="pill-txt" font-size="4.5">ROI</text><text x="229" y="173" class="pill-txt" font-size="4.5">Requirem</text><text x="229" y="178" class="pill-txt" font-size="4.5">ents</text>
    <path d="M130 205H218L214 210 218 215H130L134 210Z" class="blue-fill"/>
    <text x="174" y="212" class="pill-txt" font-size="5" font-weight="500">Common process</text>
    <path d="M232 205H322L318 210 322 215H232L236 210Z" class="blue-fill"/>
    <text x="279" y="212" class="pill-txt" font-size="5" font-weight="500">Best Practices</text>
    <path d="M223 203V214H219L225 221 231 214H227V203Z" class="blue-fill"/>
    <text x="225" y="234" class="body mid" font-size="8">Immediate Innovation</text>
  </svg>
</div>

<!-- Slide 3: Collaborating at a greater level -->
<div class="slide c3 r1">
  <svg viewBox="0 0 451 254">
    <rect class="hdr" width="451" height="53"/>
    <text x="40" y="24" class="ttl" font-size="11">Collaborating at an even greater level to achieve momentous</text>
    <text x="40" y="37" class="ttl" font-size="11">cost reduction goals.</text>
    <circle cx="418" cy="53" r="11" class="pin"/><text x="418" y="55" class="pin-num">11</text>
    <rect x="16" y="110" width="77" height="16" rx="8" class="blue-fill"/><text x="54.5" y="120" class="pill-txt">R&amp;D Industry</text>
    <rect x="16" y="136" width="77" height="16" rx="8" class="blue-fill"/><text x="54.5" y="146" class="pill-txt">Universities</text>
    <rect x="16" y="162" width="77" height="16" rx="8" class="blue-fill"/><text x="54.5" y="172" class="pill-txt">Technical Advisors</text>
    <path d="M104 133H140V125L157 142 140 159V151H104Z" class="gray-fill"/>
    <text x="128" y="141" class="pill-txt" font-size="4.8">Innovative</text><text x="128" y="146" class="pill-txt" font-size="4.8">Technology</text>
    <ellipse cx="219" cy="114" rx="48" ry="27" class="blue-fill"/>
    <text x="219" y="104" class="pill-txt">Forecast data</text>
    <text x="219" y="111" class="pill-txt">Identified opportunities</text>
    <text x="219" y="118" class="pill-txt">ROI Presentation</text>
    <text x="219" y="125" class="pill-txt">Project Planning</text>
    <ellipse cx="219" cy="185" rx="62" ry="40" class="blue-fill"/>
    <text x="219" y="160" class="pill-txt b" font-size="5">Solution Categories:</text>
    <text x="219" y="166" class="pill-txt" font-size="5">Raw Materials</text>
    <text x="219" y="172" class="pill-txt" font-size="5">Material processing</text>
    <text x="219" y="178" class="pill-txt" font-size="5">Machining</text>
    <text x="219" y="184" class="pill-txt" font-size="5">Assembly</text>
    <text x="219" y="190" class="pill-txt" font-size="5">Packaging / Transportation</text>
    <text x="219" y="196" class="pill-txt" font-size="5">Tooling &amp; Capital</text>
    <text x="219" y="202" class="pill-txt" font-size="5">Inspection &amp; Testing</text>
    <path d="M277 143L295 122V133H331V122L349 143 331 165V154H295V165Z" class="gray-fill"/>
    <text x="313" y="142" class="pill-txt" font-size="4.8">Opportunities</text><text x="313" y="147" class="pill-txt" font-size="4.8">Solutions</text>
    <rect x="354" y="129" width="82" height="30" rx="15" class="blue-fill"/>
    <text x="395" y="146.5" class="pill-txt" font-size="7.5">Supplier Group</text>
  </svg>
</div>

<!-- Slide 4: press clipping -->
<div class="slide c1 r2">
  <svg viewBox="0 0 451 254">
    <rect x="300" width="151" height="254" class="band"/>
    <circle cx="300" cy="37" r="11" class="pin"/><text x="300" y="39" class="pin-num">2</text>
    <text x="28" y="47" class="news-title">Motor Trade Daily</text>
    <text x="28" y="61" class="news-sub">Automakers' efforts to cut costs damages supplier relations, survey says</text>
    <text x="28" y="75" class="news-txt">Lena Ward</text>
    <text x="28" y="84" class="news-txt" fill="#888">Trade Desk | December 22, 2014</text>
    <text class="news-txt" font-weight="700">
      <tspan x="28" y="100">Relations between automakers and suppliers are strained by rising cost-cutting</tspan>
      <tspan x="28" y="105">demands, according to a survey.</tspan>
    </text>
    <text class="news-txt">
      <tspan x="28" y="114">Relations between automakers and suppliers are deteriorating largely because of cost</tspan>
      <tspan x="28" y="119">cutting demands, according to a new survey.</tspan>
      <tspan x="28" y="128">Vehicle makers are looking for annual price reductions of as much as 10 percent, parts</tspan>
      <tspan x="28" y="133">makers revealed in the 2014 supplier relations study by an industry consultant.</tspan>
      <tspan x="28" y="142">With few exceptions, even the best performing carmakers have become more stringent on</tspan>
      <tspan x="28" y="147">controlling costs in 2014, signaling a shift toward greater cost focus and more</tspan>
      <tspan x="28" y="152">aggressive ways to capitalize on their negotiation leverage, the study's lead author said.</tspan>
      <tspan x="28" y="161">The standard annual price reduction by automakers is about 2 to 3 percent, but it is not</tspan>
      <tspan x="28" y="166">uncommon for them to seek cuts of 5 percent or more.</tspan>
      <tspan x="28" y="175">Suppliers seem to accept that they have to find innovative ways to generate savings on a</tspan>
      <tspan x="28" y="180">year-over-year basis. However, they find it difficult to accept that they receive little</tspan>
      <tspan x="28" y="185">or no support from the OEMs in doing so, which often strains relations between the two.</tspan>
    </text>
    <text class="on-blue" font-size="7.3">
      <tspan x="316" y="160">Increasing pressure to reduce</tspan>
      <tspan x="316" y="170">costs has created a strain on</tspan>
      <tspan x="316" y="180">supplier relations.</tspan>
      <tspan x="316" y="202">Suppliers are left alone with</tspan>
      <tspan x="316" y="212">very little or no support from</tspan>
      <tspan x="316" y="222">the OEM.</tspan>
    </text>
  </svg>
</div>

<!-- Slide 5: Collaborative effort -->
<div class="slide c2 r2">
  <svg viewBox="0 0 451 254">
    <rect class="hdr" width="451" height="53"/>
    <text x="40" y="30" class="ttl">Collaborative Effort</text>
    <circle cx="418" cy="53" r="11" class="pin"/><text x="418" y="55" class="pin-num">7</text>
    <g class="small" font-size="6.6">
      <circle cx="45" cy="86" r="1.3" fill="var(--ink)"/><text x="51" y="88.5">Leveraging the power of a $3B supplier base.</text>
      <circle cx="45" cy="101" r="1.3" fill="var(--ink)"/><text x="51" y="103.5">Identifying a healthy effort towards $95M cost reduction targets.</text>
      <circle cx="45" cy="116" r="1.3" fill="var(--ink)"/><text x="51" y="118.5">Using the maximum group effort of $23M to influence cost reduction innovation.</text>
    </g>
    <rect x="114" y="143" width="225" height="81" rx="4" class="blue-fill"/>
    <line x1="226.5" y1="150" x2="226.5" y2="218" stroke="#fff" stroke-opacity=".5" stroke-width=".6"/>
    <line x1="122" y1="183.5" x2="331" y2="183.5" stroke="#fff" stroke-opacity=".5" stroke-width=".6"/>
    <text x="170" y="160" class="pill-txt" font-size="6.8">Production Forecast</text>
    <text x="282" y="160" class="pill-txt" font-size="6.8">ROI Development</text>
    <text x="170" y="212" class="pill-txt" font-size="6.8">Supplier Group Survey</text>
    <text x="282" y="212" class="pill-txt" font-size="6.8">New Model Events</text>
    <rect x="187" y="172" width="79" height="23" rx="4" class="dark-fill" stroke="#fff" stroke-width=".8"/>
    <text x="226.5" y="187.5" class="pill-txt" font-size="11">Impact</text>
  </svg>
</div>

<!-- Slide 6: Best practices -->
<div class="slide c3 r2">
  <svg viewBox="0 0 451 254">
    <rect class="hdr" width="451" height="53"/>
    <text x="40" y="30" class="ttl">Best Practices, Collaborative Effort</text>
    <circle cx="418" cy="53" r="11" class="pin"/><text x="418" y="55" class="pin-num">12</text>
    <g class="small" font-size="6.6">
      <circle cx="42" cy="82" r="1.3" fill="var(--ink)"/><text x="52" y="84.5">Incorporating best practices and shared success, supplier groups can achieve</text>
      <text x="52" y="100.5">momentous cost reduction.</text>
      <circle cx="42" cy="114" r="1.3" fill="var(--ink)"/><text x="52" y="116.5">Raw Materials.</text>
      <circle cx="42" cy="130" r="1.3" fill="var(--ink)"/><text x="52" y="132.5">Material processing.</text>
      <circle cx="42" cy="146" r="1.3" fill="var(--ink)"/><text x="52" y="148.5">Tooling &amp; Capital.</text>
      <circle cx="42" cy="162" r="1.3" fill="var(--ink)"/><text x="52" y="164.5">Machining.</text>
      <circle cx="42" cy="177" r="1.3" fill="var(--ink)"/><text x="52" y="179.5">Assembly.</text>
      <circle cx="42" cy="193" r="1.3" fill="var(--ink)"/><text x="52" y="195.5">Packaging / Transportation.</text>
      <circle cx="42" cy="209" r="1.3" fill="var(--ink)"/><text x="52" y="211.5">Inspection &amp; Testing.</text>
    </g>
  </svg>
</div>

<!-- Slide 7: Case study -->
<div class="slide c1 r3">
  <svg viewBox="0 0 451 254">
    <text x="34" y="30" class="body" font-size="12">Case Study</text>
    <rect x="30" y="45" width="180" height="121" rx="6" fill="url(#mapTone)" role="img" aria-label="Map of North America with supplier locations by region"/>
    <circle cx="270" cy="60" r="16" class="blue-fill"/>
    <text x="297" y="63" class="small" font-size="6.8"><tspan class="b">47 Automotive suppliers, NAFTA</tspan></text>
    <circle cx="270" cy="105" r="16" class="blue-fill"/>
    <text x="297" y="108" class="small" font-size="6.8"><tspan class="b">$3Billion</tspan> dollar supplier base</text>
    <circle cx="270" cy="150" r="16" class="blue-fill"/>
    <text x="297" y="148" class="small" font-size="6.8"><tspan class="b">$95Million</tspan> dollar required</text>
    <text x="297" y="157" class="small" font-size="6.8">annual cost reduction</text>
    <rect y="181" width="451" height="73" class="band"/>
    <circle cx="423" cy="182" r="11" class="pin"/><text x="423" y="184" class="pin-num">3</text>
    <text class="on-blue" font-size="6.4">
      <tspan x="30" y="210">A supplier survey was created to identify actual cost reduction impact.  The survey identified gaps between the cost</tspan>
      <tspan x="30" y="219">reduction target and individual suppliers actual effort.  A set of questions was created to help identify areas of</tspan>
      <tspan x="30" y="228">impact, ability to implement cost reduction, and the capability to measure results.</tspan>
    </text>
  </svg>
</div>

<!-- Slide 8: Strength -->
<div class="slide c2 r3">
  <svg viewBox="0 0 451 254">
    <rect class="hdr" width="451" height="53"/>
    <text x="40" y="30" class="ttl">Strength</text>
    <circle cx="418" cy="53" r="11" class="pin"/><text x="418" y="55" class="pin-num">8</text>
    <text x="288" y="68" class="small mid">Target</text>
    <rect x="249" y="74" width="78" height="74" class="blue-fill"/>
    <text x="288" y="115" class="pill-txt" font-size="12">$96M</text>
    <text x="150" y="114" class="small mid">Max Effort</text>
    <rect x="125" y="121" width="50" height="27" class="dark-fill"/>
    <text x="150" y="138" class="pill-txt" font-size="10">$23M</text>
    <line x1="125" y1="148.5" x2="327" y2="148.5" stroke="#999" stroke-width=".8"/>
    <path d="M240 149L255 175H225Z" class="dark-fill"/>
    <rect x="203" y="177" width="76" height="16" rx="8" class="blue-fill"/>
    <text x="241" y="187.5" class="pill-txt">$3B supplier base</text>
    <text x="225" y="214" class="small mid" font-size="6.2">Managing cost is more than mere price reduction.  It is a longer term strategy and requires a more</text>
    <text x="225" y="222" class="small mid" font-size="6.2">collaborative effort towards cost reduction.</text>
  </svg>
</div>

<!-- Slide 9: Project planning Venn -->
<div class="slide c3 r3">
  <svg viewBox="0 0 451 254">
    <rect class="hdr" width="451" height="53"/>
    <text x="40" y="30" class="ttl">Project planning, forecast data, ROI, GAP analysis</text>
    <circle cx="418" cy="53" r="11" class="pin"/><text x="418" y="55" class="pin-num">13</text>
    <g class="small" font-size="6.6">
      <text x="41" y="86">The products and services provided will support</text>
      <text x="41" y="102">cost reduction objectives. Which includes, a</text>
      <text x="41" y="118">proven mathematical methodology for</text>
      <text x="41" y="134">preparing ROI proposals.</text>
    </g>
    <text x="41" y="150" class="small" font-size="5.6"><tspan class="b" font-size="6.6">Example:</tspan> Using a variety of research methodologies,</text>
    <text x="41" y="156" class="small" font-size="5.6">and applied best practices we can provide support in</text>
    <text x="41" y="162" class="small" font-size="5.6">the following areas:</text>
    <text class="small" font-size="5.6">
      <tspan x="55" y="180">• Identified opportunities</tspan>
      <tspan x="55" y="189">• ROI presentation</tspan>
      <tspan x="55" y="198">• Project planning</tspan>
    </text>
    <circle cx="334" cy="116" r="43" class="venn"/>
    <circle cx="297" cy="153" r="43" class="venn"/>
    <circle cx="372" cy="153" r="43" class="venn"/>
    <circle cx="334" cy="188" r="43" class="venn"/>
    <path d="M334 120 Q346 153 334 186 Q322 153 334 120Z" class="dark-fill"/>
    <ellipse cx="334" cy="153" rx="26" ry="5" class="dark-fill"/>
    <text x="334" y="155" class="pill-txt" font-size="4">Innovation</text>
    <text x="334" y="102" class="pill-txt" font-size="4.8">Forecast data</text>
    <text x="278" y="150" class="pill-txt" font-size="4.8">Project</text><text x="278" y="156" class="pill-txt" font-size="4.8">planning</text>
    <text x="395" y="150" class="pill-txt" font-size="4.8">ROI</text><text x="385" y="156" class="pill-txt" font-size="4.8">presentation</text>
    <text x="334" y="201" class="pill-txt" font-size="4.8">GAP Analysis</text>
  </svg>
</div>

<!-- Slide 10: Supplier survey gap analysis -->
<div class="slide c1 r4">
  <svg viewBox="0 0 451 254">
    <rect width="152" height="254" class="band"/>
    <circle cx="152" cy="27" r="11" class="pin"/><text x="152" y="29" class="pin-num">4</text>
    <text x="302" y="29" class="body mid" font-size="11.5">Supplier Survey, Gap Analysis</text>
    <text class="on-blue" font-size="6.4">
      <tspan x="20" y="54">Reported areas of impact</tspan>
      <tspan x="20" y="63">towards annual cost</tspan>
      <tspan x="20" y="72">reduction requirements</tspan>
      <tspan x="20" y="90">Categories:</tspan>
      <tspan x="20" y="99">-Raw material</tspan>
      <tspan x="20" y="108">-Machine process</tspan>
      <tspan x="20" y="117">-Assembly</tspan>
      <tspan x="20" y="126">-Components</tspan>
      <tspan x="20" y="135">-Packaging</tspan>
      <tspan x="20" y="144">-Tooling</tspan>
      <tspan x="20" y="153">-Quality</tspan>
      <tspan x="20" y="171">Impact:</tspan>
      <tspan x="20" y="180">-Energy</tspan>
      <tspan x="20" y="189">-Productivity</tspan>
    </text>
    <text x="20" y="234" class="on-blue" font-size="4.4">*Add legend with color red to green best to poor</text>
    <g class="survey-table">
      <rect x="169" y="46" width="263" height="192" fill="#fff" stroke="#ccd" stroke-width=".5"/>
      <rect x="169" y="46" width="263" height="7" fill="#cfe3f6"/>
      <rect x="169" y="55" width="95" height="178" fill="url(#numLines)"/>
      <rect x="266" y="55" width="112" height="178" fill="url(#heatA)" opacity=".85"/>
      <rect x="380" y="55" width="52" height="178" fill="url(#numLines)"/>
      <rect x="169" y="233" width="263" height="5" fill="#cfe3f6"/>
      <g stroke="#dde" stroke-width=".4">
        <line x1="200" y1="46" x2="200" y2="238"/><line x1="232" y1="46" x2="232" y2="238"/>
        <line x1="264" y1="46" x2="264" y2="238"/><line x1="294" y1="46" x2="294" y2="238"/>
        <line x1="322" y1="46" x2="322" y2="238"/><line x1="350" y1="46" x2="350" y2="238"/>
        <line x1="378" y1="46" x2="378" y2="238"/><line x1="405" y1="46" x2="405" y2="238"/>
      </g>
    </g>
  </svg>
</div>

<!-- Slide 11: Supplier collaborative effort -->
<div class="slide c2 r4">
  <svg viewBox="0 0 451 254">
    <rect class="hdr" width="451" height="53"/>
    <text x="40" y="30" class="ttl">Supplier Collaborative Effort</text>
    <circle cx="418" cy="53" r="11" class="pin"/><text x="418" y="55" class="pin-num">9</text>
    <text transform="translate(78 218) rotate(-90)" class="small" font-size="5.6">Sustainable Cost &amp; Competitive Advantage</text>
    <path d="M88 220C115 150 190 102 282 100L278 80 314 104 284 148 283 126C205 126 140 160 88 220Z" class="blue-fill"/>
    <circle cx="120" cy="180" r="4" fill="#fff"/><text x="132" y="182" class="small" font-size="6" fill="#fff">Co-operation</text>
    <circle cx="174" cy="144" r="5" fill="#fff"/><text x="187" y="147" class="small" font-size="6" fill="#dff3fd">Collaborative</text>
    <circle cx="239" cy="122" r="7" fill="#fff"/>
    <text x="254" y="120" font-size="6" fill="#dff3fd">Immediate</text><text x="254" y="128" font-size="6" fill="#dff3fd">Innovation</text>
    <text x="334" y="106" class="small" font-size="6">Assured cost</text>
    <text x="334" y="114" class="small" font-size="6">reductions</text>
    <text x="89" y="229" class="small" font-size="6.2">Collaborative cost reduction</text>
  </svg>
</div>

<!-- Slide 12: Data analytics -->
<div class="slide c3 r4">
  <svg viewBox="0 0 451 254">
    <rect class="hdr" width="451" height="53"/>
    <text x="40" y="30" class="ttl">Data analytics</text>
    <circle cx="418" cy="53" r="11" class="pin"/><text x="418" y="55" class="pin-num">14</text>
    <path d="M124 118V150H150" fill="none" stroke="#ccc" stroke-width="6"/>
    <path d="M168 154V186H192" fill="none" stroke="#ccc" stroke-width="6"/>
    <line x1="186" y1="110" x2="285" y2="110" class="link"/>
    <line x1="218" y1="147" x2="285" y2="147" class="link"/>
    <line x1="265" y1="184" x2="285" y2="184" class="link"/>
    <rect x="100" y="96" width="86" height="28" rx="14" class="blue-fill"/><text x="143" y="112.5" class="pill-txt">Survey</text>
    <rect x="144" y="132" width="74" height="29" rx="14.5" class="blue-fill"/><text x="181" y="149" class="pill-txt">Forecast data</text>
    <rect x="187" y="169" width="78" height="29" rx="14.5" class="blue-fill"/><text x="226" y="186" class="pill-txt">ROI</text>
    <text x="290" y="112.5" class="small" font-size="6.6">Effort</text>
    <text x="290" y="149.5" class="small" font-size="6.6">Events &amp; timing</text>
    <text x="290" y="186.5" class="small" font-size="6.6">Solutions</text>
  </svg>
</div>

<!-- Slide 13: Individual effort not enough -->
<div class="slide c1 r5">
  <svg viewBox="0 0 451 254">
    <rect class="hdr" width="451" height="53"/>
    <text x="40" y="30" class="ttl">Individual Supplier Effort Is Not Enough</text>
    <circle cx="418" cy="53" r="11" class="pin"/><text x="418" y="55" class="pin-num">5</text>
    <path d="M162.7 121.1A56 56 0 1 1 117 93V119A30 30 0 1 0 141.5 131.8Z" class="blue-fill"/>
    <path d="M122 87A56 56 0 0 1 168 114L145 127A30 30 0 0 0 122 113Z" fill="#d2cbd8"/>
    <rect x="191" y="112" width="81" height="20" fill="#cfcfd4"/>
    <text x="231.5" y="120" class="pill-txt" font-size="5.8">$5.7M Actual impact</text>
    <text x="231.5" y="128" class="pill-txt" font-size="5.8">on cost reduction</text>
    <rect x="191" y="146" width="81" height="20" class="blue-fill"/>
    <text x="231.5" y="154" class="pill-txt" font-size="5.8">$96M Required</text>
    <text x="231.5" y="162" class="pill-txt" font-size="5.8">cost reduction</text>
    <rect x="306" y="77" width="40" height="132" class="blue-fill"/>
    <text x="311" y="184" class="on-blue" font-size="5.2">Supplier</text><text x="311" y="190" class="on-blue" font-size="5.2">Base</text><text x="311" y="196" class="on-blue" font-size="5.2">Condition</text>
    <rect x="351" y="179" width="40" height="30" class="blue-fill"/>
    <text x="355" y="186" class="on-blue" font-size="5.2">Suppliers</text><text x="355" y="192" class="on-blue" font-size="5.2">Individual</text><text x="355" y="198" class="on-blue" font-size="5.2">Efforts</text>
    <line x1="370" y1="77" x2="370" y2="177" stroke="var(--blue)" stroke-width=".6" stroke-dasharray="2 2"/>
    <rect x="352" y="113" width="36" height="24" fill="#fff"/>
    <text x="370" y="121" class="small mid b" font-size="5">-4% Cost</text>
    <text x="370" y="127" class="small mid b" font-size="5">Reduction</text>
    <text x="370" y="133" class="small mid b" font-size="5">Target</text>
    <text x="225" y="232" class="small mid" font-size="6.2">Missed cost reduction targets, supplier accepts loss and is forced to operate with lower margins</text>
  </svg>
</div>

<!-- Slide 14: Going beyond -->
<div class="slide c2 r5">
  <svg viewBox="0 0 451 254">
    <rect class="hdr" width="451" height="53"/>
    <text x="40" y="24" class="ttl" font-size="11">Going beyond even the most advanced supplier collaboration and</text>
    <text x="40" y="37" class="ttl" font-size="11">innovative models and inviting strategic innovation opportunities</text>
    <circle cx="418" cy="53" r="11" class="pin"/><text x="418" y="55" class="pin-num">10</text>
    <g class="bulb" fill="none" stroke="#222" stroke-width="1.2" stroke-linecap="round">
      <circle cx="51" cy="140" r="12"/>
      <path d="M46 152V158H56V152M47 161H55"/>
      <path d="M51 118V123M33 140H24M69 140H78M37 126L32 121M65 126L70 121M36 129L28 133M66 129L74 133"/>
    </g>
    <path d="M87 122H130V114L144 142 130 170V162H87Z" class="blue-fill"/>
    <text x="91" y="140" class="on-blue" font-size="5">Innovative</text>
    <text x="91" y="146" class="on-blue" font-size="5">Technology</text>
    <rect x="148" y="115" width="114" height="51" class="blue-fill"/>
    <text x="205" y="127" class="pill-txt" font-size="7.5">Forecast data</text>
    <text x="205" y="137" class="pill-txt" font-size="7.5">ROI Presentation</text>
    <text x="205" y="147" class="pill-txt" font-size="7.5">Identified opportunities</text>
    <text x="205" y="157" class="pill-txt" font-size="7.5">Project Planning</text>
    <path d="M266 141L282 122V130H318V122L334 141 318 160V152H282V160Z" class="blue-fill"/>
    <text x="300" y="140" class="pill-txt" font-size="5">Opportunities</text>
    <text x="300" y="146" class="pill-txt" font-size="5">Solutions</text>
    <rect x="339" y="117" width="103" height="47" rx="16" class="photo" role="img" aria-label="Dark grey sedan"/>
    <text x="225" y="202" class="small mid" font-size="6.2">Integrating technology providers into the cost improvement strategy</text>
  </svg>
</div>

<!-- Slide 15: Next steps -->
<div class="slide c3 r5">
  <svg viewBox="0 0 451 254">
    <rect class="hdr" width="451" height="53"/>
    <text x="40" y="30" class="ttl">Next Steps</text>
    <circle cx="418" cy="53" r="11" class="pin"/><text x="418" y="55" class="pin-num">15</text>
    <g class="stairs">
      <rect x="38" y="96" width="74" height="158" class="step-front"/>
      <path d="M38 96L44 90H118L112 96Z" class="step-top"/>
      <path d="M112 96L118 90V130L112 134Z" class="step-side"/>
      <rect x="112" y="134" width="35" height="120" class="step-front"/>
      <path d="M112 134L118 128H153L147 134Z" class="step-top"/>
      <path d="M147 134L153 128V166L147 172Z" class="step-side"/>
      <rect x="147" y="172" width="33" height="82" class="step-front"/>
      <path d="M147 172L153 166H186L180 172Z" class="step-top"/>
      <path d="M180 172L186 166V201L180 207Z" class="step-side"/>
      <rect x="180" y="207" width="27" height="47" class="step-front"/>
      <path d="M180 207L186 201H213L207 207Z" class="step-top"/>
      <path d="M207 207L213 201V254H207Z" class="step-side"/>
    </g>
    <line x1="118" y1="104" x2="142" y2="104" class="link"/>
    <line x1="153" y1="140" x2="174" y2="140" class="link"/>
    <line x1="186" y1="177" x2="206" y2="177" class="link"/>
    <line x1="213" y1="214" x2="235" y2="214" class="link"/>
    <circle cx="153" cy="104" r="11" class="num-ring"/><text x="153" y="107.5" class="num">1</text>
    <circle cx="185" cy="140" r="11" class="num-ring"/><text x="185" y="143.5" class="num">2</text>
    <circle cx="217" cy="177" r="11" class="num-ring"/><text x="217" y="180.5" class="num">3</text>
    <circle cx="246" cy="214" r="11" class="num-ring"/><text x="246" y="217.5" class="num">4</text>
    <text x="177" y="107" class="body" font-size="7.8">Build advisor group</text>
    <text x="209" y="143" class="body" font-size="7.8">Proposal for Kaiyo Motors</text>
    <text x="241" y="180" class="body" font-size="7.8">Marcus's relationship with Kaiyo NAP</text>
    <text x="270" y="217" class="body" font-size="7.8">Meeting with Kaiyo R&amp;D purchasing</text>
  </svg>
</div>

</body>
</html>
```